KVT Building And Maintenance

Need a very professional looking double sided Buisiness card with all my details phone number, name, email, license number.

Target Market(s)

construction industry

Industry/Entity Type

building

Contact Information for Business Card

Name Dale Pemberton. Email Address Info@KVTBuilding.com.au mobile number 0452918736 licence number 671093D. web site

```html
<!DOCTYPE html>
<html lang="en">
<head>
<meta charset="utf-8">
<title>KVT Building And Maintenance – Business Card</title>
<link href="https://fonts.googleapis.com/css2?family=Saira:wght@400;600;700&display=swap" rel="stylesheet">
<style>
  :root {
    --canvas: #ececec;
    --card-white: #ffffff;
    --card-black: #050708;
    --band-grey: #262626;
    --brand-blue: #3f9ad6;
    --logo-grey: #4a4a4a;
    --text-light: #f2f2f2;
    --pattern-a: #1c1c1c;
    --pattern-b: #0b0d0e;
  }
  * { margin: 0; padding: 0; box-sizing: border-box; }
  html, body { width: 1200px; height: 1200px; overflow: hidden; }
  body {
    background: var(--canvas);
    font-family: "Saira", sans-serif;
    position: relative;
  }
  .card {
    position: absolute;
    top: 480px;
    width: 420px;
    height: 240px;
    overflow: hidden;
  }
  .card--front { left: 158px; background: var(--card-white); }
  .card--back { left: 623px; background: var(--card-black); }

  .front-art { position: absolute; inset: 0; }

  .brand-name {
    position: absolute;
    left: 14px;
    top: 20px;
    color: var(--logo-grey);
    font-weight: 700;
    line-height: 0.95;
    text-transform: uppercase;
  }
  .brand-name__main { display: block; font-size: 50px; letter-spacing: 1px; }
  .brand-name__sub { display: block; font-size: 24px; letter-spacing: 0.5px; }

  .holder-name {
    position: absolute;
    right: 17px;
    top: 84px;
    color: var(--brand-blue);
    font-weight: 700;
    font-size: 20px;
    letter-spacing: 0.3px;
  }
  .contact-list {
    position: absolute;
    right: 16px;
    top: 130px;
    list-style: none;
    text-align: right;
  }
  .contact-list li {
    color: var(--text-light);
    font-size: 11.5px;
    line-height: 16px;
    display: flex;
    justify-content: flex-end;
    align-items: center;
    gap: 5px;
  }
  .contact-list svg { width: 11px; height: 11px; fill: var(--brand-blue); }
  .licence {
    position: absolute;
    right: 17px;
    top: 192px;
    color: var(--text-light);
    font-size: 11.5px;
  }
  .licence__number { color: var(--brand-blue); }

  .back-pattern {
    position: absolute;
    inset: 0;
    background: repeating-linear-gradient(180deg, var(--pattern-a) 0 3px, var(--pattern-b) 3px 18px);
  }
  .back-brand {
    position: absolute;
    left: 37px;
    top: 148px;
    color: var(--card-white);
    font-weight: 700;
    font-size: 38px;
    letter-spacing: 1px;
    text-transform: uppercase;
  }
</style>
</head>
<body>
  <section class="card card--front" aria-label="Business card front">
    <svg class="front-art" width="420" height="240" viewBox="0 0 420 240">
      <defs>
        <linearGradient id="bandShade" x1="0" y1="0" x2="1" y2="0">
          <stop offset="0" stop-color="#0a0a0a"/>
          <stop offset="0.6" stop-color="#2a2a2a"/>
          <stop offset="1" stop-color="#1a1a1a"/>
        </linearGradient>
      </defs>
      <polygon class="dark-panel" points="307,0 420,0 420,220 86,220" fill="var(--card-black)"/>
      <polygon class="shade-band" points="200,107 230,107 161,220 118,220" fill="url(#bandShade)" opacity="0.8"/>
      <line class="accent-diagonal" x1="294" y1="0" x2="137" y2="157" stroke="var(--brand-blue)" stroke-width="1.2"/>
      <line class="accent-rule" x1="76" y1="230" x2="284" y2="230" stroke="var(--brand-blue)" stroke-width="1.2"/>
    </svg>

    <div class="brand-name">
      <span class="brand-name__main">KVT</span>
      <span class="brand-name__sub">Building</span>
    </div>

    <h1 class="holder-name">Dale Pemberton</h1>
    <ul class="contact-list">
      <li>045 291 8736
        <svg viewBox="0 0 24 24" aria-hidden="true"><path d="M6.6 10.8a15 15 0 0 0 6.6 6.6l2.2-2.2c.3-.3.7-.4 1-.2 1.1.4 2.3.6 3.6.6.6 0 1 .4 1 1V20c0 .6-.4 1-1 1A17 17 0 0 1 3 4c0-.6.4-1 1-1h3.5c.6 0 1 .4 1 1 0 1.3.2 2.5.6 3.6.1.3 0 .7-.2 1z"/></svg>
      </li>
      <li>Info@KVTBuilding.com.au
        <svg viewBox="0 0 24 24" aria-hidden="true"><path d="M2 5h20v14H2z M3 6l9 7 9-7" /><path d="M2 5l10 8 10-8" fill="none" stroke="#050708" stroke-width="1.6"/></svg>
      </li>
      <li>www.KVTBuilding.com.au
        <svg viewBox="0 0 24 24" aria-hidden="true"><circle cx="12" cy="12" r="10"/><path d="M2 12h20M12 2c3 3 3 17 0 20M12 2c-3 3-3 17 0 20" fill="none" stroke="#050708" stroke-width="1.4"/></svg>
      </li>
    </ul>
    <p class="licence">licence number <span class="licence__number">671093D</span></p>
  </section>

  <section class="card card--back" aria-label="Business card back">
    <div class="back-pattern" role="img" aria-label="Dark repeating chevron pattern background"></div>
    <div class="back-brand">KVT Building</div>
  </section>
</body>
</html>
```